Logo Tweak & Full Set of Stationery

We need a redesign / tweaking of Logo for rebranding of our company. We are Australia's largest installer of commercial fencing and high security infrastructure. We also have divisions in security and civil works (infrastrucuture).

We would like to see designs that incorporate black, white & blue. Revamp of current Diamond Logo (including HC) would be ideal but open to all ideas.

Design needs to portray a highly professional & corporate image.

Required:
- Tweak / Redesign of Logo
- Letterhead
- email Signature
- Business Cards
- Presentation Folder

Address fields should be interchangeable to accomodate multiple locations.

Website: www.harvillecorp.com.au
Updates

Due to short turn around time for project - Fee increased to $500 AUD Guaranteed

Thanks

Designs are looking good
I have emailed those submitted thus far to the board to start short listing.

Please do not take offence if your design is eliminated as part of this process  - there are so many great concepts and if is difficult to pick between them.

Thanks
Dustin

Target Market(s)

Tier 1 / 2 Builders (ie.. Brick Arch Peter Farley) and Government related bodies

Industry/Entity Type

Security

Requirements
Must have
• Company Name: Harville Corp

Tag Line: Fencing * Security * Civil

Logo

```html
<!DOCTYPE html>
<html lang="en">
<head>
<meta charset="utf-8">
<title>Harville Corp – Identity &amp; Business Card</title>
<link rel="stylesheet" href="https://fonts.googleapis.com/css2?family=Barlow:wght@400;600&family=Arimo:wght@400;700&display=swap">
<style>
  :root {
    --ink: #1f1f1f;
    --ink-soft: #3a3a3a;
    --paper: #ffffff;
    --band: #e1e2e3;
    --card-dark: #4a4a4a;
    --card-dark-edge: #3b3b3b;
    --brand-blue: #1d5fa6;
    --brand-blue-light: #7fb3e6;
  }
  * { margin: 0; padding: 0; box-sizing: border-box; }
  html, body { width: 1200px; height: 846px; overflow: hidden; background: var(--paper); }
  .canvas { position: relative; width: 1200px; height: 846px; overflow: hidden; background: var(--paper); }

  .hero { position: absolute; left: 0; top: 0; width: 1200px; height: 408px; background: var(--paper); }
  .hero__square { position: absolute; left: 232px; top: 150px; width: 104px; height: 104px; background: var(--brand-blue); }
  .hero__name { position: absolute; left: 367px; top: 150px; font-family: "Barlow", sans-serif; font-weight: 600; font-size: 88px; line-height: 1; color: var(--ink); letter-spacing: -0.5px; }
  .hero__entity { position: absolute; left: 369px; top: 243px; font-family: "Barlow", sans-serif; font-weight: 400; font-size: 44px; line-height: 1; color: var(--ink); }
  .hero__tagline { position: absolute; left: 371px; top: 306px; font-family: "Barlow", sans-serif; font-weight: 600; font-size: 20px; line-height: 1; letter-spacing: 3px; text-transform: uppercase; color: var(--brand-blue); }

  .band { position: absolute; left: 0; top: 408px; width: 1200px; height: 438px; background: var(--band); }

  .card { position: absolute; top: 460px; width: 521px; height: 318px; box-shadow: 0 1px 4px rgba(0,0,0,0.25); }
  .card--front { left: 59px; background: var(--paper); }
  .card--back { left: 607px; background: var(--card-dark); color: var(--paper); text-align: center; }

  .card__square { position: absolute; left: 30px; top: 46px; width: 56px; height: 56px; background: var(--brand-blue); }
  .card__brand { position: absolute; left: 117px; top: 50px; font-family: "Barlow", sans-serif; font-weight: 600; font-size: 38px; line-height: 1; color: var(--ink); }
  .card__entity { position: absolute; left: 118px; top: 88px; font-family: "Barlow", sans-serif; font-size: 22px; line-height: 1; color: var(--ink); }
  .card__tagline { position: absolute; left: 119px; top: 114px; font-family: "Barlow", sans-serif; font-weight: 600; font-size: 11px; line-height: 1; letter-spacing: 1.5px; text-transform: uppercase; color: var(--brand-blue); }

  .contact { position: absolute; left: 118px; top: 140px; font-family: "Arimo", sans-serif; color: var(--ink); }
  .contact__name { font-family: "Barlow", sans-serif; font-size: 28px; line-height: 1; }
  .contact__role { font-size: 12px; text-transform: uppercase; margin-top: 4px; color: var(--ink-soft); }
  .contact__line { font-size: 16px; line-height: 19px; }
  .contact__line b, .office b { font-weight: 700; }

  .office { position: absolute; right: 30px; top: 244px; text-align: right; font-family: "Arimo", sans-serif; font-size: 14px; line-height: 18px; color: var(--ink); }

  .card__texture { position: absolute; inset: 0; background: radial-gradient(circle at 50% 40%, #555 0%, var(--card-dark) 55%, var(--card-dark-edge) 100%); }
  .services { position: relative; padding-top: 48px; font-family: "Arimo", sans-serif; }
  .services__title { font-weight: 700; font-size: 19px; line-height: 25px; }
  .services__list { margin-top: 22px; font-size: 11.5px; line-height: 14.5px; padding: 0 30px; }
  .services__web { margin-top: 20px; font-weight: 700; font-size: 19px; color: var(--brand-blue-light); }
</style>
</head>
<body>
<main class="canvas">
  <section class="hero">
    <div class="hero__square"></div>
    <div class="hero__name">Harville Corp</div>
    <div class="hero__entity">Australia Pty Ltd</div>
    <div class="hero__tagline">Fencing &#8226; Security &#8226; Civil</div>
  </section>

  <section class="band"></section>

  <article class="card card--front">
    <div class="card__square"></div>
    <div class="card__brand">Harville Corp</div>
    <div class="card__entity">Australia Pty Ltd</div>
    <div class="card__tagline">Fencing &#8226; Security &#8226; Civil</div>
    <div class="contact">
      <div class="contact__name">Dustin Whitford</div>
      <div class="contact__role">Chief Financial Officer</div>
      <div class="contact__line">dwhitford@harvillecorp.com.au</div>
      <div class="contact__line"><b>M:</b> +61 4 1300 5521</div>
    </div>
    <div class="office">
      <div><b>FREE CALL:</b> 1800 555 014</div>
      <div><b>T:</b> +61 2 9555 0146 &nbsp;<b>F:</b> +61 2 9555 0175</div>
      <div>www.harvillecorp.com.au</div>
    </div>
  </article>

  <article class="card card--back">
    <div class="card__texture" role="img" aria-label="Dark chainwire mesh texture"></div>
    <div class="services">
      <div class="services__title">We Specialise in ALL types<br>of Fencing &amp; Security Systems</div>
      <p class="services__list">
        Palisade Fencing, Tubular Security Fencing, CF358 Security Mesh,<br>
        Chainwire Fencing (permanent &amp; temporary), Guard Rails and Handrails,<br>
        Internal Chainwire Enclosures, Weldmesh Fencing and Enclosures,<br>
        Non-Destructive Digging, Livestock and Fauna Fencing, Access Control,<br>
        Security Systems, Bollards, Security Lighting, Alarm Systems, Civil Works,<br>
        Type 1-6 RTA Approved Pedestrian Fencing, Wire Rope Vehicle Fencing,<br>
        Rock Fall Fencing, Electronic Fencing and ALL Styles of Gates to suit.
      </p>
      <div class="services__web">www.harvillecorp.com.au</div>
    </div>
  </article>
</main>
</body>
</html>
```